Cleaning Service Company In need of Good Web presence.

The company is a cleaning service company which provides professional staff and service for cleaning. This is a project to build a site that is both solid and a strong recognition of our organization. It is supposed to show quality, cleanliness, professionalism. The use of images and art for imagery is all good just to have a site that is consistent and solid. There might be a chance to make stationary, logo and business cars if someone feels they can build a brand that is consistent. The image we are going for is clean solid and to stand out. Finally stationary should not be expensive to print.

Current logo is attached and can be used or can be made more creative.

Target Market(s)

Corporate and Government entities, that will feel that this company has a brand that sets it apart from the rest. The company is new so the modification of the logo will not be an issue if a more solid brand come out of this project. The idea is to have a clean consistent product that stands our from others in terms of website, stationary, etc

Industry/Entity Type

Cleaning Service

Contact Information for Business Card

P.O.Box 51947
Riffa
Kingdom of Bahrain

Logo Text

Brightmoor Facility Care

Number of Pages Required

4 page

Font styles to use
Sans Serif

Colors
abd036
cadf82
eaf2ce
9bcb3b

Requirements
Must have
• Green Color to be used in order to stick to the name. Also the creativity and boldness in an elegant manner.
Nice to have
• Arabic name of company
• برايتمور فاسيليتي كير ذ.م.م
• if cannot be put at least make a location should be chosen
• Also could be a bit of 3D given to the logo if it could stay elegent.
Should not have
• Should not show people cleaning.

```html
<!DOCTYPE html>
<html lang="en">
<head>
<meta charset="utf-8">
<title>Brightmoor Facility Care</title>
<link href="https://fonts.googleapis.com/css2?family=Exo+2:wght@200;300;400;600;700&family=Open+Sans:wght@400;600;700&family=Raleway:wght@700&display=swap" rel="stylesheet">
<style>
:root{
  --lime:#9bcb3b;
  --lime-soft:#abd036;
  --green:#0a8a1c;
  --forest:#067a3c;
  --dark:#444444;
  --charcoal:#4d4d4d;
  --footer:#3a3a3a;
  --ink:#333333;
  --muted:#888888;
  --light:#f4f4f4;
  --white:#ffffff;
}
*{margin:0;padding:0;box-sizing:border-box}
html,body{width:1200px;height:2956px;overflow:hidden}
body{font-family:"Open Sans",sans-serif;color:var(--ink);background:var(--white);position:relative}
.abs{position:absolute}

/* top bar */
.topbar{top:0;left:0;width:1200px;height:40px;background:var(--white)}
.topbar .info{position:absolute;top:10px;font-size:15px;color:#333;display:flex;align-items:center;gap:6px}
.topbar svg{width:15px;height:15px}
.navband{top:40px;left:0;width:1200px;height:46px;background:var(--lime);z-index:2}
.nav{position:absolute;left:438px;top:0;display:flex;height:46px;align-items:center}
.nav a{color:var(--white);text-decoration:none;font-size:15px;margin-right:0;position:relative;letter-spacing:.3px}
.nav a.active::after{content:"";position:absolute;left:0;right:0;bottom:-12px;height:3px;background:var(--forest)}
.logo{top:10px;left:108px;width:138px;height:138px;border-radius:50%;background:var(--white);border:6px solid var(--lime);z-index:3;display:flex;align-items:center;justify-content:center;text-align:center;font-family:"Exo 2",sans-serif;font-weight:700;font-size:17px;line-height:1.15;color:var(--green)}

/* hero */
.hero{top:86px;left:0;width:1200px;height:531px;background:linear-gradient(180deg,#2f6aa6 0%,#3a7cbc 45%,#2a4c74 75%,#1b2330 100%)}
.hero h1{position:absolute;left:106px;top:126px;font-family:"Exo 2",sans-serif;font-weight:600;font-size:42px;line-height:50px;color:var(--white)}
.hero .tag{position:absolute;left:110px;top:240px;font-size:15px;color:var(--white)}
.hero .callbtn{position:absolute;left:110px;top:292px;width:202px;height:44px;border:1px solid var(--white);display:flex;align-items:center}
.callbtn .ic{width:48px;height:42px;background:var(--white);display:flex;align-items:center;justify-content:center}
.callbtn span{color:var(--white);font-weight:700;font-size:16px;margin-left:22px}

/* info boxes */
.infobox{top:670px;height:142px;width:308px;display:flex;align-items:center;overflow:hidden}
.infobox .tri{position:absolute;left:0;top:0}
.infobox .ico{position:absolute;left:16px;top:56px}
.infobox .txt{position:absolute;left:102px;top:48px;color:var(--white)}
.infobox .sm{font-size:13px;line-height:16px}
.infobox .big{font-family:"Exo 2",sans-serif;font-size:19px;line-height:22px}

/* welcome */
.eyebrow{top:862px;left:0;width:1200px;text-align:center;color:var(--lime);font-weight:700;font-size:15px}
.title{top:884px;left:0;width:1200px;text-align:center;font-family:"Exo 2",sans-serif;font-weight:200;font-size:40px;color:#333}
.lead{top:954px;left:330px;width:540px;text-align:center;font-size:12px;line-height:21px;color:#666}
.rule{top:1025px;left:560px;width:80px;height:1px;background:#aaa}

.hub{top:1070px;left:418px;width:366px;height:366px;border-radius:50%;background:radial-gradient(circle at 50% 35%,#bcd3ea 0%,#7f9fbf 45%,#6a5a4a 78%,#c06a2a 100%)}
.svc-ic{width:108px;height:108px;border-radius:50%;border:5px solid var(--white);display:flex;align-items:center;justify-content:center}
.svc{width:226px}
.svc h3{font-family:"Exo 2",sans-serif;font-weight:600;font-size:16px;color:#333;margin-bottom:6px}
.svc p{font-size:12px;line-height:21px;color:#999}
.svc .line{height:1px;background:#bbb;margin-top:10px}
.svc.right{text-align:left}.svc.left{text-align:right}

/* services band */
.band-photo{top:1556px;left:0;width:567px;height:465px;background:linear-gradient(180deg,#c4d9ea 0%,#9dbcd4 40%,#4c7a6c 70%,#1d9cae 100%)}
.band{top:1556px;left:567px;width:633px;height:465px;background:var(--forest);color:var(--white)}
.band h2{position:absolute;left:30px;top:28px;font-family:"Exo 2",sans-serif;font-weight:600;font-size:29px}
.band .sub{position:absolute;left:35px;top:70px;font-size:17px}
.band ul{position:absolute;left:35px;top:118px;list-style:none}
.band li{font-size:14px;height:30.3px;display:flex;align-items:center;gap:14px;padding-left:2px}
.band .more{position:absolute;left:42px;top:378px;width:136px;height:42px;border:1px solid var(--white);display:flex;align-items:center;justify-content:center;font-size:16px}

/* testimonial */
.testi{top:2021px;left:0;width:1200px;height:416px;background:var(--light)}
.testi h2{position:absolute;top:28px;width:1200px;text-align:center;font-family:"Raleway",sans-serif;font-weight:700;font-size:30px;color:#333}
.testi .bar{position:absolute;top:82px;left:525px;width:136px;height:3px;background:var(--forest)}
.testi blockquote{position:absolute;top:130px;left:118px;width:964px;text-align:center;font-style:italic;font-size:15px;line-height:26px;color:#444}
.avatar{position:absolute;top:200px;left:543px;width:84px;height:84px;border-radius:50%;border:3px solid var(--forest);background:linear-gradient(180deg,#d5d9dc,#9aa3aa)}
.testi .name{position:absolute;top:300px;width:1200px;text-align:center;font-weight:700;font-size:15px}
.testi .role{position:absolute;top:324px;width:1200px;text-align:center;font-size:15px;color:#555}
.dots{position:absolute;top:365px;left:550px;display:flex;gap:6px}
.dots i{width:14px;height:3px;background:#777;display:block}
.dots i:first-child{background:var(--forest)}

/* contact */
.contact{top:2437px;left:0;width:1200px;height:455px;background:var(--charcoal);color:var(--white)}
.contact h2{position:absolute;left:117px;top:72px;font-family:"Exo 2",sans-serif;font-weight:400;font-size:31px}
.contact .intro{position:absolute;left:117px;top:124px;width:540px;font-size:15px;line-height:22px}
.citem{position:absolute;left:112px;display:flex;align-items:center;gap:14px;font-size:14px;line-height:20px}
.citem .dot{width:42px;height:42px;border-radius:50%;background:var(--white);display:flex;align-items:center;justify-content:center;flex:none}
.field{position:absolute;border:1px solid #ddd;color:#eee;font-size:13px;padding:10px 12px}
.submit{position:absolute;left:514px;top:368px;width:108px;height:40px;background:#262626;color:var(--white);font-size:14px;display:flex;align-items:center;justify-content:center}
.footer{top:2892px;left:0;width:1200px;height:64px;background:var(--footer);color:#eee;font-size:14px;display:flex;align-items:center;justify-content:center}
</style>
</head>
<body>

<div class="abs topbar">
  <div class="info" style="left:760px"><svg viewBox="0 0 16 16"><rect width="16" height="16" rx="3" fill="#0a8a1c"/><path d="M5 3.5l2 2-1 1.5c.7 1.4 1.6 2.3 3 3l1.5-1 2 2-1.2 1.6C8 12.5 3.5 8 3.4 4.7z" fill="#fff"/></svg>1-877-540-2219</div>
  <div class="info" style="left:898px"><svg viewBox="0 0 16 16"><circle cx="8" cy="8" r="6.5" fill="none" stroke="#0a8a1c" stroke-width="2"/><path d="M8 4.5V8l2.5 1.5" stroke="#0a8a1c" stroke-width="1.6" fill="none"/></svg>24/7 emergency serive</div>
</div>

<div class="abs navband">
  <nav class="nav">
    <a class="active" style="margin-right:66px">HOME</a>
    <a style="margin-right:64px">SERVICES</a>
    <a style="margin-right:64px">PROJECTS</a>
    <a style="margin-right:64px">NEWS</a>
    <a style="margin-right:64px">ABOUT US</a>
    <a>CONTACT</a>
  </nav>
</div>
<div class="abs logo">Brightmoor<br>Facility<br>Care</div>

<section class="abs hero" role="img" aria-label="Night skyline of a waterfront city with twin sail-shaped towers and lights reflected in the bay">
  <h1>More Than 450 Facilities<br>Cleaned Every day</h1>
  <p class="tag">Your Preferred Cleaning Service Company</p>
  <div class="callbtn"><div class="ic"><svg width="20" height="20" viewBox="0 0 16 16"><path d="M4 1.5l2.5 2.5-1.2 1.8c.8 1.7 2 2.9 3.6 3.7l1.8-1.2 2.5 2.5-1.5 2C6.5 12.5 2 8 1.8 3z" fill="#222"/></svg></div><span>1-877-540-2219</span></div>
</section>

<div class="abs infobox" style="left:112px;background:var(--lime)">
  <svg class="tri" width="80" height="142"><polygon points="0,0 80,71 0,142" fill="#444"/></svg>
  <svg class="ico" width="32" height="32" viewBox="0 0 32 32"><circle cx="16" cy="17" r="12" fill="none" stroke="#fff" stroke-width="2"/><path d="M16 9v8l-4 3" stroke="#fff" stroke-width="2" fill="none"/></svg>
  <div class="txt"><div class="sm">We are open Mon - Fri</div><div class="big">Mon-Fri 08:00-17:00</div></div>
</div>
<div class="abs infobox" style="left:445px;background:var(--green)">
  <svg class="tri" width="80" height="142"><polygon points="0,0 80,71 0,142" fill="#111"/></svg>
  <svg class="ico" width="34" height="34" viewBox="0 0 32 32"><path d="M16 4a8 8 0 0 0-8 8c0 6 8 14 8 14s8-8 8-14a8 8 0 0 0-8-8z" fill="none" stroke="#fff" stroke-width="2"/><circle cx="16" cy="12" r="3" fill="none" stroke="#fff" stroke-width="2"/><path d="M6 26h20" stroke="#fff" stroke-width="2"/></svg>
  <div class="txt"><div class="big">Located in</div><div class="sm">Building 214, Road 18, Riffa</div></div>
</div>
<div class="abs infobox" style="left:780px;background:var(--lime)">
  <svg class="tri" width="80" height="142"><polygon points="0,0 80,71 0,142" fill="#444"/></svg>
  <svg class="ico" width="36" height="30" viewBox="0 0 36 30"><rect x="2" y="4" width="32" height="22" fill="none" stroke="#fff" stroke-width="2"/><path d="M2 4l16 13L34 4M2 26l12-11M34 26L22 15" stroke="#fff" stroke-width="2" fill="none"/></svg>
  <div class="txt"><div class="big">Drop a Massage</div><div class="sm">hello@brightmoorcare.bh</div></div>
</div>

<p class="abs eyebrow">WELCOME TO OUR SITE</p>
<h2 class="abs title">Professional Cleaning Service</h2>
<p class="abs lead">Pulvinar odio volutpat. Quam temere in vitiis, legem sancimus haerentia. Qui ipsorum lingua Celtae, nostra Galli appellantur. Non equidem invideo, miror magis posuere velit aliquet. Ut enim ad minim veniam</p>
<div class="abs rule"></div>

<div class="abs hub" role="img" aria-label="Round photo of a modern city skyline with twin towers at dusk"></div>

<div class="abs svc left" style="left:110px;top:1082px"><h3>Commercial Cleaning</h3><p>Class aptent taciti sociosqu ad litora torquent per conubia nostra....</p><div class="line"></div></div>
<div class="abs svc right" style="left:862px;top:1082px"><h3>Residention Cleaning</h3><p>Class aptent taciti sociosqu ad litora torquent per conubia nostra....</p><div class="line"></div></div>
<div class="abs svc left" style="left:110px;top:1332px"><h3>Vehicle Cleaning</h3><p>Class aptent taciti sociosqu ad litora torquent per conubia nostra....</p><div class="line"></div></div>
<div class="abs svc right" style="left:862px;top:1332px"><h3>Tiling &amp; Painting</h3><p>Class aptent taciti sociosqu ad litora torquent per conubia nostra....</p><div class="line"></div></div>

<div class="abs svc-ic" style="left:356px;top:1073px;background:var(--green)"><svg width="40" height="40" viewBox="0 0 40 40" fill="none" stroke="#fff" stroke-width="2"><path d="M6 8l10 4 18 22M16 12l-6 12M16 12l4 14M16 12l10 10"/></svg></div>
<div class="abs svc-ic" style="left:736px;top:1073px;background:var(--lime)"><svg width="40" height="40" viewBox="0 0 40 40" fill="none" stroke="#fff" stroke-width="2"><path d="M8 26v-8l4-7h16l4 7v8zM8 26v4h4v-4M28 26v4h4v-4M8 18h24"/><circle cx="13" cy="22" r="1.5"/><circle cx="27" cy="22" r="1.5"/></svg></div>
<div class="abs svc-ic" style="left:356px;top:1323px;background:var(--lime)"><svg width="40" height="40" viewBox="0 0 40 40" fill="none" stroke="#fff" stroke-width="2"><path d="M26 6l8 8-10 10-8-8zM16 16l-8 14 4 4 14-8M12 26l6-6"/></svg></div>
<div class="abs svc-ic" style="left:736px;top:1323px;background:var(--lime)"><svg width="40" height="40" viewBox="0 0 40 40" fill="none" stroke="#fff" stroke-width="2"><rect x="8" y="5" width="22" height="9"/><path d="M30 9h4v9H20v5"/><rect x="17" y="23" width="6" height="12"/></svg></div>

<div class="abs band-photo" role="img" aria-label="Daytime photo of a waterfront business district with a tall tower and green island"></div>
<section class="abs band">
  <h2>BFC SERVICES</h2>
  <p class="sub">Lorem Ipsum is simply dummy text of the printing.</p>
  <ul>
    <li><svg width="16" height="14" viewBox="0 0 16 14" fill="none" stroke="#fff" stroke-width="1.3"><rect x="1" y="1" width="14" height="12" rx="2"/><path d="M4 7l3 3 5-6"/></svg>Lorem Ipsum is simply dummy text of the printing</li>
    <li><svg width="16" height="14" viewBox="0 0 16 14" fill="none" stroke="#fff" stroke-width="1.3"><rect x="1" y="1" width="14" height="12" rx="2"/><path d="M4 7l3 3 5-6"/></svg>Typesetting industry. Lorem Ipsum has been the industry's</li>
    <li><svg width="16" height="14" viewBox="0 0 16 14" fill="none" stroke="#fff" stroke-width="1.3"><rect x="1" y="1" width="14" height="12" rx="2"/><path d="M4 7l3 3 5-6"/></svg>Standard dummy text ever since the 1500s,</li>
    <li><svg width="16" height="14" viewBox="0 0 16 14" fill="none" stroke="#fff" stroke-width="1.3"><rect x="1" y="1" width="14" height="12" rx="2"/><path d="M4 7l3 3 5-6"/></svg>When an unknown printer took a galley of type and scramble</li>
    <li><svg width="16" height="14" viewBox="0 0 16 14" fill="none" stroke="#fff" stroke-width="1.3"><rect x="1" y="1" width="14" height="12" rx="2"/><path d="M4 7l3 3 5-6"/></svg>Lorem Ipsum is simply dummy text of the printing</li>
    <li><svg width="16" height="14" viewBox="0 0 16 14" fill="none" stroke="#fff" stroke-width="1.3"><rect x="1" y="1" width="14" height="12" rx="2"/><path d="M4 7l3 3 5-6"/></svg>Typesetting industry. Lorem Ipsum has been the industry's</li>
    <li><svg width="16" height="14" viewBox="0 0 16 14" fill="none" stroke="#fff" stroke-width="1.3"><rect x="1" y="1" width="14" height="12" rx="2"/><path d="M4 7l3 3 5-6"/></svg>Standard dummy text ever since the 1500s,</li>
    <li><svg width="16" height="14" viewBox="0 0 16 14" fill="none" stroke="#fff" stroke-width="1.3"><rect x="1" y="1" width="14" height="12" rx="2"/><path d="M4 7l3 3 5-6"/></svg>When an unknown printer took a galley of type and scramble</li>
  </ul>
  <div class="more">More Services</div>
</section>

<section class="abs testi">
  <h2>WHAT OUR CLIENT SAY</h2>
  <div class="bar"></div>
  <blockquote>" Suscipit lobortis dolor sit amet, consectetuer adipiscing elit, sed diam nonummy nibh euismod tincidunt ut laoreet dolore magna aliquam erat volutpat. Ut wisi enim ad minim veniam, quis nostrud exerci tation ullamcorper suscipit lobortis."</blockquote>
  <div class="avatar" role="img" aria-label="Client portrait photo"></div>
  <p class="name">Mariam Al-Sayed</p>
  <p class="role">Professtional Details</p>
  <div class="dots"><i></i><i></i><i></i></div>
</section>

<section class="abs contact">
  <h2>GET IN TOUCH</h2>
  <p class="intro">Lorem Ipsum is simply dummy text of the printing and typesetting industry. Lorem Ipsum has been the industry's</p>
  <div class="citem" style="top:196px"><div class="dot"><svg width="16" height="20" viewBox="0 0 16 20"><path d="M8 1a6 6 0 0 0-6 6c0 5 6 12 6 12s6-7 6-12a6 6 0 0 0-6-6z" fill="#0a8a1c"/><circle cx="8" cy="7" r="2.2" fill="#fff"/></svg></div><span>simply dummy text of the printing and<br>typesetting industry</span></div>
  <div class="citem" style="top:262px"><div class="dot"><svg width="20" height="16" viewBox="0 0 20 16" fill="none" stroke="#0a8a1c" stroke-width="1.8"><rect x="1" y="1" width="18" height="14" rx="2"/><path d="M1 2l9 7 9-7"/></svg></div><span>info@brightmoorcare.bh</span></div>
  <div class="citem" style="top:330px"><div class="dot"><svg width="18" height="18" viewBox="0 0 16 16"><path d="M4 1.5l2.5 2.5-1.2 1.8c.8 1.7 2 2.9 3.6 3.7l1.8-1.2 2.5 2.5-1.5 2C6.5 12.5 2 8 1.8 3z" fill="#0a8a1c"/></svg></div><span>+973-1755-0421</span></div>
  <div class="field" style="left:514px;top:206px;width:252px;height:42px">Name</div>
  <div class="field" style="left:514px;top:258px;width:252px;height:42px">Number</div>
  <div class="field" style="left:514px;top:310px;width:252px;height:42px">Mail</div>
  <div class="field" style="left:787px;top:206px;width:306px;height:152px">Message</div>
  <div class="submit">SUBMIT</div>
</section>

<footer class="abs footer">All rights reserved Copyright © 2017 Brightmoor Facility Care</footer>

</body>
</html>
```